Business card design needed

I need a business card design for a dog walking, dog minding and dog training business. Please refer to my website for the basic company colours and fonts I'm after. Planning on a double sided card, so all information doesn't need to be on the 'front' side.
Cheers

Industry/Entity Type

Dog Training

Contact Information for Business Card

Meadow Paws - happy hounds
Rua 0498307164
meadowpawsdemo.com.au
-walking
-holiday stays
-onsite care
-training and behavioural consultations

```html
<!DOCTYPE html>
<html lang="en">
<head>
<meta charset="utf-8">
<title>Meadow Paws – Business Card</title>
<link rel="stylesheet" href="https://fonts.googleapis.com/css2?family=Open+Sans:wght@300;400&family=Didact+Gothic&display=swap">
<style>
  :root {
    --orange: #e8622a;
    --orange-soft: #f0a070;
    --ink: #2b2b2b;
    --grey-text: #3a3a3a;
    --band-top: #f7f7f7;
    --band-bottom: #e6e6e6;
    --card-bg: #f4f4f4;
    --white: #ffffff;
  }
  html, body {
    margin: 0;
    padding: 0;
    width: 1200px;
    height: 682px;
    overflow: hidden;
    background: var(--white);
  }
  .card {
    position: relative;
    width: 1200px;
    height: 682px;
    overflow: hidden;
    background: linear-gradient(180deg, var(--white) 0%, var(--card-bg) 60%, var(--white) 100%);
    font-family: "Open Sans", sans-serif;
  }
  .header-band {
    position: absolute;
    left: 0; top: 35px;
    width: 1200px; height: 172px;
    background: linear-gradient(180deg, var(--band-top) 0%, #fdfdfd 35%, var(--band-bottom) 100%);
    border-top: 1px solid #e4e4e4;
  }
  .brand-name {
    position: absolute;
    left: 46px; top: 42px;
    margin: 0;
    font-family: "Open Sans", sans-serif;
    font-weight: 400;
    font-size: 62px;
    line-height: 1;
    letter-spacing: -1px;
    color: var(--orange);
    white-space: nowrap;
  }
  .running-dogs {
    position: absolute;
    left: 440px; top: 40px;
    width: 520px; height: 135px;
    background: radial-gradient(ellipse at 60% 45%, rgba(180,180,180,0.35), rgba(220,220,220,0) 70%);
  }
  .tagline {
    position: absolute;
    left: 739px; top: 104px;
    margin: 0;
    font-family: "Didact Gothic", sans-serif;
    font-size: 22px;
    color: var(--grey-text);
    white-space: nowrap;
  }
  .puppy-photo {
    position: absolute;
    left: 922px; top: 63px;
    width: 220px; height: 128px;
    border-radius: 60px 60px 10px 10px;
    background: linear-gradient(180deg, #c98a55 0%, #f1efec 55%, #e8e6e3 100%);
  }
  .paw-art {
    position: absolute;
    left: 58px; top: 248px;
    width: 357px; height: 392px;
    border-radius: 45%;
    background: radial-gradient(circle at 50% 55%, #e8622a 0%, #d9561f 45%, rgba(232,98,42,0) 72%);
  }
  .faint-dog-photo {
    position: absolute;
    left: 910px; top: 346px;
    width: 255px; height: 300px;
    background: radial-gradient(ellipse at 50% 45%, rgba(215,210,200,0.45), rgba(240,240,240,0) 70%);
  }
  .details {
    position: absolute;
    left: 511px; top: 382px;
    width: 647px;
  }
  .detail-row {
    display: flex;
    justify-content: space-between;
    white-space: nowrap;
  }
  .label {
    font-weight: 300;
    font-size: 34px;
    line-height: 44px;
    color: var(--orange);
  }
  .value {
    font-weight: 400;
    font-size: 31px;
    line-height: 46px;
    color: var(--ink);
  }
  .right { text-align: right; }
  .divider {
    position: absolute;
    left: 511px; top: 506px;
    width: 656px; height: 20px;
  }
  .for-heading {
    position: absolute;
    left: 511px;
    top: 510px;
    width: 656px;
    margin: 0;
    text-align: center;
    font-family: "Didact Gothic", sans-serif;
    font-weight: 400;
    font-size: 42px;
    letter-spacing: 3px;
    line-height: 1;
    color: var(--orange);
    transform: scaleX(1.3);
  }
  .services {
    position: absolute;
    left: 511px; top: 563px;
    width: 660px;
    font-weight: 300;
    font-size: 36px;
    line-height: 41px;
    color: var(--ink);
    white-space: nowrap;
  }
  .services-row { display: block; }
  .sep { color: var(--orange); margin: 0 8px; }
</style>
</head>
<body>
<main class="card">
  <div class="header-band"></div>
  <div class="running-dogs" role="img" aria-label="Faint grey silhouettes of dogs running across the header"></div>
  <h1 class="brand-name">MEADOW PAWS</h1>
  <p class="tagline">happy hounds</p>
  <div class="puppy-photo" role="img" aria-label="Photo of a brown and white puppy peeking over the edge"></div>

  <div class="paw-art" role="img" aria-label="Large orange paw print illustration"></div>
  <div class="faint-dog-photo" role="img" aria-label="Faded background photo of a dog"></div>

  <section class="details">
    <div class="detail-row">
      <span class="label">Contacts</span>
      <span class="label right">Website</span>
    </div>
    <div class="detail-row">
      <span class="value">Rua 0498307164</span>
      <span class="value right">meadowpawsdemo.com.au</span>
    </div>
  </section>

  <svg class="divider" viewBox="0 0 656 20" aria-hidden="true">
    <line x1="0" y1="3" x2="656" y2="3" stroke="#f0a070" stroke-width="3"/>
    <line x1="0" y1="9" x2="656" y2="9" stroke="#e8622a" stroke-width="3"/>
    <line x1="0" y1="16" x2="140" y2="16" stroke="#f0a070" stroke-width="3"/>
    <line x1="516" y1="16" x2="656" y2="16" stroke="#f0a070" stroke-width="3"/>
  </svg>
  <h2 class="for-heading">For</h2>

  <section class="services">
    <div class="services-row">Walking<span class="sep">|</span>Holiday stays<span class="sep">|</span>Onsite care</div>
    <div class="services-row">Training and Behavioural&nbsp; consultations</div>
  </section>
</main>
</body>
</html>
```